A Freight forwarding (transportation/shipping) company requires stationary design

We need The following:
1. Letterhead
2. Letter Envelope
3. A4 Paper Envelope
4. A4 Paper Folder (One that is 2xA4 foldable size which we can open in half and we can put a paper in between)
5. A5 Paper (To be used for notes taking)

a design for a freight forwarding company named VORELTA DUNIMOR INTERNATIONAL TRANSPORTATION CO . Business Card is already designed and should follow it, the files attached help guide you in type of docs required + Logos (We are active in Sea Transportation, Truck transportation, and Air Transportation, (printed design is required with all open source files for editing - lamination accepted)

The said company is agent and sales representative of 2 other Shipping companies (whose logos, name, and website should also be mentioned on Envelopes and Folder) - Bold Wave and TQN Shipping, logos attached.

Bold Wave Shipping LLC
Dubai, United Arab Emirates
www.bwsmarine-example.com

TQN Shipping Line Ltd
London, United Kingdom
www.tqnlinex-example.com

Address is "No.7, 2nd Soltani-e-Norvand, Tehran, IR
Tel number is +98 21 55302914
Fax number is +98 21 55306631
E-Mail address is info@voreltadunimor-example.com
Website is www.voreltadunimor-example.com

```html
<!DOCTYPE html>
<html lang="en">
<head>
<meta charset="utf-8">
<title>Vorelta Dunimor – A4 Folder</title>
<link rel="stylesheet" href="https://fonts.googleapis.com/css2?family=Ubuntu:wght@400;500&display=swap">
<style>
  :root {
    --stage: #b8b8b8;
    --navy-dark: #0b3049;
    --navy: #0f3d5a;
    --navy-light: #124766;
    --paper: #ffffff;
    --paper-shade: #e9e9e9;
    --brand-blue: #2f4f9c;
    --contact-ink: #d7e2ea;
    --ring: #9aa0a6;
  }
  * { margin: 0; padding: 0; box-sizing: border-box; }
  html, body { width: 1200px; height: 814px; overflow: hidden; }
  body {
    background: var(--stage);
    font-family: "Ubuntu", sans-serif;
    position: relative;
  }
  .folder {
    position: absolute;
    left: 77px;
    top: 37px;
    width: 1046px;
    height: 740px;
    display: flex;
    box-shadow: 0 12px 30px rgba(0,0,0,0.25);
  }
  .folder-back {
    position: relative;
    width: 523px;
    height: 100%;
    background: linear-gradient(160deg, var(--navy-dark) 0%, var(--navy) 55%, var(--navy-light) 100%);
  }
  .back-watermark {
    position: absolute;
    left: 0;
    right: 0;
    top: 250px;
    text-align: center;
    font-size: 40px;
    font-weight: 500;
    color: rgba(255,255,255,0.05);
    letter-spacing: 1px;
    line-height: 1.2;
  }
  .contact {
    position: absolute;
    left: 46px;
    bottom: 52px;
    list-style: none;
    color: var(--contact-ink);
    font-size: 9.5px;
    line-height: 13px;
  }
  .contact li { display: flex; align-items: center; gap: 5px; }
  .contact .address { padding-left: 0; }
  .contact svg { width: 8px; height: 8px; fill: var(--contact-ink); flex: none; }
  .folder-front {
    position: relative;
    width: 523px;
    height: 100%;
    background: linear-gradient(150deg, var(--paper) 0%, var(--paper) 60%, var(--paper-shade) 100%);
    overflow: hidden;
  }
  .brand {
    position: absolute;
    left: 0;
    right: 0;
    top: 205px;
    display: flex;
    flex-direction: column;
    align-items: center;
  }
  .brand-circle {
    width: 150px;
    height: 150px;
    border-radius: 50%;
    border: 3px solid var(--ring);
    margin-bottom: 18px;
  }
  .brand-name {
    color: var(--brand-blue);
    font-size: 17px;
    font-weight: 500;
    text-align: center;
    line-height: 21px;
  }
  .pocket {
    position: absolute;
    left: 0;
    bottom: 0;
    width: 523px;
    height: 70px;
  }
</style>
</head>
<body>
  <main class="folder">
    <section class="folder-back">
      <div class="back-watermark">Vorelta Dunimor</div>
      <ul class="contact">
        <li class="address">No.7, 2nd Soltani-e-Norvand,</li>
        <li class="address">Tehran, IR</li>
        <li><svg viewBox="0 0 10 10"><path d="M2 0h2l1 3-1.5 1a6 6 0 0 0 2.5 2.5L7 5l3 1v2a2 2 0 0 1-2 2A8 8 0 0 1 0 2a2 2 0 0 1 2-2z"/></svg>+98 21 55302914</li>
        <li><svg viewBox="0 0 10 10"><path d="M2 0h6v3H2zM0 4h10v4H8v2H2V8H0zM3 7v2h4V7z"/></svg>+98 21 55306631</li>
        <li><svg viewBox="0 0 10 10"><path d="M0 2h10v6H0zM1 3l4 3 4-3"/></svg>info@voreltadunimor-example.com</li>
        <li><svg viewBox="0 0 10 10"><circle cx="5" cy="5" r="5"/></svg>www.voreltadunimor-example.com</li>
      </ul>
    </section>
    <section class="folder-front">
      <div class="brand">
        <div class="brand-circle"></div>
        <p class="brand-name">Vorelta Dunimor<br>International<br>Transport.Co L.L.c</p>
      </div>
      <svg class="pocket" viewBox="0 0 523 70" preserveAspectRatio="none" aria-hidden="true">
        <path d="M0 22 H420 Q430 22 434 14 Q438 6 448 6 H523 V70 H0 Z" fill="#0f3d5a"/>
        <path d="M0 28 H422 Q432 28 436 20 Q440 12 450 12 H523" fill="none" stroke="#ffffff" stroke-width="1.5"/>
      </svg>
    </section>
  </main>
</body>
</html>
```